Visitenkarten-Design für Gästehaus und Küche in der Fußgängerzone
Zielgruppe
Gästehaus und Küche in der Fußgängerzone, zwei Gehminuten zum Bodensee.
Neu renoviertes Hotel/Restaurant (z.B.Boxspringbett, Holzboden, USB Steckdosen).
Übernachtung mit Frühstück im Einzel,-Doppel,- oder Komfortzimmer (für 3 Personen).
Restaurant mit regionaler Küche. Besondere saisonale Zutaten unserer Nachbarländer als Specials.
Touristen im Sommer Durchschnittalter: 50 Jahre, sportlich, modern, gut betucht.
Einwohner der Stadt im Winter, Alter zwischen 25 und 65 Jahre, viele davon Hausbesitzer, Segelboot Besitzer etc.
Aufgabenstellung
Farbkonzept im Restaurant:
warm- weiße Wände, dunkle Holzmöbel, rote Barelemente, weiß-kupferfarbene Lampen.
Würden uns etwas minimalistisches wünschen, trotzdem mit einem Wow Effekt.
Sei es ein ausgeschnittenes Logo, abgerundete Ecken, besonderes Material usw.
Dateianhänge sind nur für´s bessere Verständnis, muss nicht zwingend als Vorgabe gesehen werden.
Vorderseite:
Logo
Hotel & Restaurant (kann, muss aber nicht draufstehen.)
zum Anker
Seewalden

```html
<!DOCTYPE html>
<html lang="de">
<head>
<meta charset="utf-8">
<title>zum Anker – Visitenkarten</title>
<link rel="stylesheet" href="https://fonts.googleapis.com/css2?family=Quicksand:wght@300;400;600&display=swap">
<style>
  :root {
    --bg-top: #f4f4f4;
    --bg-bottom: #dcdcdc;
    --card: #ffffff;
    --copper: #a46b1c;
    --ink: #1e1e1e;
    --ink-soft: #5a5a5a;
  }
  * { box-sizing: border-box; margin: 0; padding: 0; }
  html, body { width: 1200px; height: 802px; overflow: hidden; }
  body {
    background: linear-gradient(160deg, var(--bg-top), var(--bg-bottom));
    font-family: "Quicksand", sans-serif;
    color: var(--ink);
    display: flex;
    align-items: center;
    justify-content: center;
    gap: 60px;
  }
  .card {
    position: relative;
    width: 510px;
    height: 330px;
    background: var(--card);
    border-radius: 4px;
    overflow: hidden;
    box-shadow: 0 10px 30px rgba(0,0,0,.18);
  }
  .card__band {
    position: absolute;
    inset: 0;
    width: 100%;
    height: 100%;
  }
  .card__band path { fill: var(--copper); }

  /* Front */
  .front__brand {
    position: absolute;
    top: 78px;
    left: 0;
    right: 0;
    display: flex;
    flex-direction: column;
    align-items: center;
  }
  .brand__name {
    font-size: 42px;
    font-weight: 600;
    color: var(--ink);
    line-height: 1;
  }
  .brand__town {
    margin-top: 10px;
    font-size: 15px;
    font-weight: 300;
    letter-spacing: 2px;
    color: var(--ink-soft);
  }
  .brand__tagline {
    margin-top: 4px;
    font-size: 15px;
    font-weight: 300;
    letter-spacing: 3px;
    color: var(--ink-soft);
  }

  /* Back */
  .back__address {
    position: absolute;
    top: 42px;
    left: 0;
    right: 0;
    font-size: 21px;
    font-weight: 400;
    font-style: normal;
    line-height: 1.2;
    text-align: center;
  }
  .back__contacts {
    position: absolute;
    top: 118px;
    left: 36px;
    list-style: none;
    font-size: 19px;
    font-weight: 400;
    line-height: 1.5;
  }
  .back__contacts li {
    display: flex;
    align-items: center;
    gap: 12px;
  }
  .contact__icon {
    width: 20px;
    height: 20px;
    fill: none;
    stroke: var(--ink);
    stroke-width: 1.4;
    stroke-linejoin: round;
    stroke-linecap: round;
  }
</style>
</head>
<body>

  <section class="card card--back" aria-label="Rückseite">
    <svg class="card__band" viewBox="0 0 510 330" preserveAspectRatio="none" aria-hidden="true">
      <path d="M0 190 C 140 240 330 250 510 300 L510 330 L0 330 Z"/>
    </svg>
    <address class="back__address">
      Seegasse 14<br>88699 Seewalden
    </address>
    <ul class="back__contacts">
      <li>
        <svg class="contact__icon" viewBox="0 0 24 24" aria-hidden="true"><path d="M6 3l3 4-2 2c1 3 4 6 7 7l2-2 4 3-2 4C10 21 3 14 2 5z"/></svg>
        07599 482617
      </li>
      <li>
        <svg class="contact__icon" viewBox="0 0 24 24" aria-hidden="true"><rect x="2" y="5" width="20" height="14"/><path d="M2 5l10 8 10-8"/></svg>
        info@zum-anker-seewalden.de
      </li>
      <li>
        <svg class="contact__icon" viewBox="0 0 24 24" aria-hidden="true"><path d="M3 11l9-8 9 8M5 10v11h14V10M10 21v-6h4v6"/></svg>
        www.zum-anker-seewalden.de
      </li>
    </ul>
  </section>

  <section class="card card--front" aria-label="Vorderseite">
    <svg class="card__band" viewBox="0 0 510 330" preserveAspectRatio="none" aria-hidden="true">
      <path d="M0 175 C 130 250 330 265 510 295 L510 330 L0 330 Z"/>
    </svg>
    <div class="front__brand">
      <span class="brand__name">zum Anker</span>
      <span class="brand__town">Seewalden</span>
      <span class="brand__tagline">Gästehaus und Küche</span>
    </div>
  </section>

</body>
</html>
```